Seven Banner Campaigns Need Them Now

I want banners created for 7 campaigns.
For each campaign I need these 6 banner sizes created:
Web Banner Sizes (300x250, 728x90, 160x600)
One of each of these sizes, so 3 web banners
Mobile Banner Sizes (300x50, 216x36, 240x240)
campaign 1
Water emergency restoration
http://www.mendwavelocal.example/
http://www.nearbyshopratings.example/Lincoln-Park-MI/TKV-Recovery-60557.html
campaign2
Highway Sparrow Auto Coverage
http://www.nearbyshopratings.example/Houston-TX/HSAC-Shieldline-60581.html
campaign 3
Velora Free Health Insurance quotes
http://www.nearbyshopratings.example/Velora-66185.html
campaign4
Thrifty Shades
www.nearbyshopratings.example/Aberdeen-SD/Thrifty-Shades-of-Aberdeen-Watertown-and-Sisseton-64613.html
campaign5
Rebuild Masters
http://www.nearbyshopratings.example/Bathroom-Remodeling-Contractors-64668.html
Want to focus on the right contractor for all your home project and remodeling needs
campaign 6
Lasik Eye Surgery
http://www.townlistpages.example/m/beverly-hills-ca-lasik/
http://www.clearsightcenter.example/csc-micro/index.html?venid=Search&subid=QRTB&pid=5550172043&gclid=ZXKPqRTWmNbAFYHJTLpd7GKqRs
focus on a free evaluation with a Lasik specialist
campaign 7
QRX
cash for cars.  focus on sell your junker car for fast cash
we will even come pick it up!
http://www.townlistpages.example/m/spokane-wa-cash-for-cars/
Need these done ASAP..more to come!

Industry/Entity Type
Contractor
Requirements
Must have
- Phone call call to action on each banner

```html
<!DOCTYPE html>
<html lang="en">
<head>
<meta charset="utf-8">
<title>Local Contractors Banner Set</title>
<link rel="stylesheet" href="https://fonts.googleapis.com/css2?family=Arimo:wght@400;700&display=swap">
<style>
  :root {
    --teal: #1db4bf;
    --teal-deep: #14a3ae;
    --ink: #0d0d0d;
    --white: #ffffff;
    --orange-top: #ffc526;
    --orange-bottom: #ff8a00;
    --orange-edge: #e07400;
    --photo-light: #e3cfb2;
    --photo-dark: #8d7860;
    --stage-top: #ffffff;
    --stage-bottom: #e4e4e4;
  }
  html, body {
    margin: 0;
    width: 1200px;
    height: 900px;
    overflow: hidden;
  }
  body {
    background: linear-gradient(180deg, var(--stage-top) 0%, var(--stage-top) 20%, var(--stage-bottom) 100%);
    font-family: "Arimo", Arial, sans-serif;
  }
  .stage {
    position: absolute;
    left: 0;
    top: 0;
    width: 1024px;
    height: 768px;
    transform: scale(1.171875);
    transform-origin: 0 0;
  }
  .banner {
    position: absolute;
    overflow: hidden;
    background: linear-gradient(180deg, var(--teal) 0%, var(--teal-deep) 100%);
  }
  .banner svg.photo { position: absolute; left: 0; top: 0; }
  .headline {
    position: absolute;
    margin: 0;
    color: var(--ink);
    font-weight: 700;
    text-align: center;
    line-height: 1.1;
  }
  .call-now {
    position: absolute;
    margin: 0;
    color: var(--white);
    font-weight: 700;
    text-align: center;
    line-height: 1;
  }
  .phone-button {
    position: absolute;
    display: flex;
    align-items: center;
    justify-content: center;
    color: var(--white);
    font-weight: 700;
    background: linear-gradient(180deg, var(--orange-top) 0%, var(--orange-bottom) 100%);
    border: 1px solid var(--orange-edge);
    box-shadow: 0 2px 3px rgba(0,0,0,0.35), inset 0 1px 0 rgba(255,255,255,0.5);
    text-shadow: 0 1px 1px rgba(120,50,0,0.6);
    white-space: nowrap;
  }

  /* 160x600 skyscraper */
  .skyscraper { left: 89px; top: 135px; width: 160px; height: 600px; }
  .skyscraper .headline { left: 0; width: 160px; top: 210px; font-size: 33px; line-height: 1.42; }
  .skyscraper .headline .small-line { display: block; font-size: 20px; line-height: 1.2; }
  .skyscraper .call-now { left: 0; width: 160px; top: 487px; font-size: 22px; }
  .skyscraper .phone-button { left: 3px; top: 515px; width: 150px; height: 36px; border-radius: 12px; font-size: 20px; }

  /* 216x36 mobile */
  .mobile-small { left: 612px; top: 203px; width: 216px; height: 36px; }
  .mobile-small .headline { left: 58px; width: 68px; top: 3px; font-size: 8.5px; line-height: 1.15; }
  .mobile-small .call-now { left: 130px; width: 76px; top: 3px; font-size: 9px; }
  .mobile-small .phone-button { left: 128px; top: 14px; width: 78px; height: 15px; border-radius: 5px; font-size: 9px; }

  /* 300x50 mobile */
  .mobile-wide { left: 570px; top: 262px; width: 300px; height: 50px; }
  .mobile-wide .headline { left: 84px; width: 86px; top: 3px; font-size: 12px; line-height: 1.15; }
  .mobile-wide .call-now { left: 182px; width: 106px; top: 4px; font-size: 12.5px; }
  .mobile-wide .phone-button { left: 182px; top: 20px; width: 106px; height: 21px; border-radius: 7px; font-size: 12.5px; }

  /* 240x240 mobile square */
  .square-mobile { left: 401px; top: 368px; width: 240px; height: 240px; }
  .square-mobile .headline { left: 0; width: 240px; top: 96px; font-size: 24px; }
  .square-mobile .call-now { left: 0; width: 240px; top: 161px; font-size: 23px; }
  .square-mobile .phone-button { left: 22px; top: 189px; width: 190px; height: 40px; border-radius: 14px; font-size: 22px; }

  /* 300x250 medium rectangle */
  .rectangle { left: 666px; top: 358px; width: 300px; height: 250px; }
  .rectangle .headline { left: 0; width: 300px; top: 105px; font-size: 24px; }
  .rectangle .call-now { left: 0; width: 300px; top: 171px; font-size: 23px; }
  .rectangle .phone-button { left: 48px; top: 197px; width: 202px; height: 40px; border-radius: 14px; font-size: 22px; }

  /* 728x90 leaderboard */
  .leaderboard { left: 264px; top: 645px; width: 728px; height: 90px; }
  .leaderboard .headline { left: 250px; width: 276px; top: 12px; font-size: 27px; line-height: 1.42; }
  .leaderboard .call-now { left: 518px; width: 200px; top: 10px; font-size: 23px; }
  .leaderboard .phone-button { left: 515px; top: 38px; width: 204px; height: 40px; border-radius: 14px; font-size: 22px; }
</style>
</head>
<body>
<div class="stage">
  <svg width="0" height="0" style="position:absolute">
    <defs>
      <linearGradient id="photoTone" x1="0" y1="0" x2="1" y2="1">
        <stop offset="0" stop-color="#e3cfb2"/>
        <stop offset="0.55" stop-color="#c2a98a"/>
        <stop offset="1" stop-color="#8d7860"/>
      </linearGradient>
    </defs>
  </svg>

  <section class="banner skyscraper">
    <svg class="photo" width="160" height="160" viewBox="0 0 160 160">
      <path d="M0 0 H160 V45 Q140 132 0 150 Z" fill="url(#photoTone)" role="img" aria-label="Bright bathroom interior photo with freestanding tub and vanity"/>
      <path d="M160 45 Q140 132 0 150" fill="none" stroke="#fff" stroke-width="5"/>
    </svg>
    <h2 class="headline">Looking<br>for<br>Local<span class="small-line">Contractors?</span></h2>
    <p class="call-now">Call Now!</p>
    <div class="phone-button">(888) 555-0142</div>
  </section>

  <section class="banner mobile-small">
    <svg class="photo" width="60" height="36" viewBox="0 0 60 36">
      <path d="M0 0 H58 Q46 24 28 36 H0 Z" fill="url(#photoTone)" role="img" aria-label="Bathroom interior photo"/>
      <path d="M58 0 Q46 24 28 36" fill="none" stroke="#fff" stroke-width="2"/>
    </svg>
    <h2 class="headline">Looking for Local Contractors?</h2>
    <p class="call-now">Call Now!</p>
    <div class="phone-button">(888) 555-0142</div>
  </section>

  <section class="banner mobile-wide">
    <svg class="photo" width="86" height="50" viewBox="0 0 86 50">
      <path d="M0 0 H84 Q66 34 40 50 H0 Z" fill="url(#photoTone)" role="img" aria-label="Bathroom interior photo"/>
      <path d="M84 0 Q66 34 40 50" fill="none" stroke="#fff" stroke-width="2.5"/>
    </svg>
    <h2 class="headline">Looking for Local Contractors?</h2>
    <p class="call-now">Call Now!</p>
    <div class="phone-button">(888) 555-0142</div>
  </section>

  <section class="banner square-mobile">
    <svg class="photo" width="240" height="100" viewBox="0 0 240 100">
      <path d="M8 0 A112 88 0 0 0 232 0 Z" fill="url(#photoTone)" role="img" aria-label="Bathroom interior photo with tub and vanity"/>
      <path d="M8 0 A112 88 0 0 0 232 0" fill="none" stroke="#fff" stroke-width="4"/>
    </svg>
    <h2 class="headline">Looking for Local<br>Contractors?</h2>
    <p class="call-now">Call Now!</p>
    <div class="phone-button">(888) 555-0142</div>
  </section>

  <section class="banner rectangle">
    <svg class="photo" width="300" height="100" viewBox="0 0 300 100">
      <path d="M24 0 A126 92 0 0 0 276 0 Z" fill="url(#photoTone)" role="img" aria-label="Bathroom interior photo with tub and vanity"/>
      <path d="M24 0 A126 92 0 0 0 276 0" fill="none" stroke="#fff" stroke-width="4"/>
    </svg>
    <h2 class="headline">Looking for Local<br>Contractors?</h2>
    <p class="call-now">Call Now!</p>
    <div class="phone-button">(888) 555-0142</div>
  </section>

  <section class="banner leaderboard">
    <svg class="photo" width="256" height="90" viewBox="0 0 256 90">
      <path d="M0 0 H250 Q252 56 236 90 H0 Z" fill="url(#photoTone)" role="img" aria-label="Bathroom interior photo with tub and vanity"/>
      <path d="M250 0 Q252 56 236 90" fill="none" stroke="#fff" stroke-width="4"/>
    </svg>
    <h2 class="headline">Looking for Local<br>Contractors?</h2>
    <p class="call-now">Call Now!</p>
    <div class="phone-button">(888) 555-0142</div>
  </section>
</div>
</body>
</html>
```